Tourism Marketing needing sleek, clear design for business card & proposal documents.

***Company background***
"Quiet Harbour" is a company specializing in tourism marketing and project management. We do international wholesale, event management as well as ongoing representation of tourism and hospitality companies.

***Target market***
We cater to tourism companies and hotel professionals.

***Task***
We would like to get a single sided business card designed (but will still consider two sided, we are open to any ideas you may have). The layout for this card should be modern and elegant. Currently we do not have a logo, but we would like our business name in a really simple typography for the business card (similar to Merrow Lounge's logo - www.merrowlounge.com.au).We are after a design that is clear, strong enough to be recognised as Quiet Harbour that does not require any fancy design. Another option is a simple play on QH (Quiet Harbour) or simply have Quiet Harbour featured elsewhere on card more as a brand/logo.

Feel free to submit different fonts if you feel you have any other fonts/designs that may be suitable for this card other than sans serifs. Should this project be successful, we will be considering several other projects for business proposal templates and eventually a website design.

The information that needs to go on the card are as follows:

Odette Farrow
Director
Quiet Harbour
Tourism Marketing & Representation
57 Wendlow Terrace
Harrowdene, Westmark, 2719 Australia
T +61 428306172 E odette@quietharbour.com.au

***Look and feel***
We'd like the business card design to express the following:
Modern, sleek, elegant, simple, discreet, quality, subtle, professional, creative, innovation

In terms of typography, we like something really simple and blocky (similar font to Merrow Lounge's logo - www.merrowlounge.com.au)

***Colour scheme***
Shades of grey and dark teal

***Note***
Although our main target market are professionals, we would like the business card design to be versatile enough to be used outside of the tourism industry and need to appeal to different markets.

I do not have existing logo. Was hoping for a design that may be clear, strong enough not to require one. Other option is a simple play on QH (Quiet Harbour) or simply have Quiet Harbour featured elsewhere on card more as a brand/logo.

Odette Farrow
Director
Quiet Harbour Pty Ltd 
57 Wendlow Terrace
T +61 428306172  E  odette@quietharbour.com.au

Thank you for designs so far. Many have used a mauve colour which matches our company profile. This is not necessary, as that is just a draft and will be completely redesigned, so dont  feel you need to incorporate the mauve.

My colour preferences are for a white or grey background, and I like fonts in dark teals, grey or other sophisticated but modern colours. feel free to submit different fonts if you you have other fonts you thing would be suitable for this card, along with sans serifs. Should this project be successful, we will be considering several others for business proposal templates and eventually website. 

Target Market(s)

International Hospitality Senior Executives, Directors of International Tourism Companies, Directors of Tourism Bodies Internationally, local Tourism

Industry/Entity Type

Hospitality

Requirements
Should not have
• must not have bright garish colour, swirly patterns or anything that dates too much.

```html
<!DOCTYPE html>
<html lang="en">
<head>
<meta charset="utf-8">
<title>Quiet Harbour – Business Card</title>
<link rel="stylesheet" href="https://fonts.googleapis.com/css2?family=Lora:wght@400;500&display=swap">
<style>
  :root {
    --page: #eeeeee;
    --teal: #174560;
    --silver-light: #f1f1f1;
    --silver-dark: #c9c9c9;
    --ink-light: #e3e6e8;
    --ink-muted: #b9c5cd;
    --card-shadow: rgba(0, 0, 0, 0.14);
  }
  * { margin: 0; padding: 0; box-sizing: border-box; }
  html, body {
    width: 1200px; height: 795px; overflow: hidden;
    background: var(--page);
    font-family: "Lora", Georgia, serif;
  }
  .sheet {
    position: relative; width: 1200px; height: 795px;
    display: flex; align-items: center; justify-content: center; gap: 60px;
  }
  .card {
    position: relative; width: 520px; height: 297px; overflow: hidden;
    box-shadow: 0 10px 24px var(--card-shadow);
  }
  .card-bg { position: absolute; inset: 0; }

  /* Back side */
  .card-back { background: var(--teal); }
  .card-back .brand {
    position: absolute; left: 0; right: 0; top: 118px; text-align: center;
    color: var(--ink-light);
  }
  .brand-name {
    font-weight: 400; letter-spacing: 0.06em; text-transform: uppercase;
    font-size: 24px; line-height: 1;
  }
  .brand-tagline { font-size: 13px; margin-top: 6px; letter-spacing: 0.02em; }

  /* Front side */
  .card-front .brand {
    position: absolute; left: 150px; right: 20px; top: 34px; text-align: center;
    color: var(--teal);
  }
  .card-front .brand-name { font-weight: 500; font-size: 22px; }
  .card-front .brand-tagline { font-size: 12px; }

  .person { position: absolute; left: 30px; top: 122px; color: var(--ink-light); }
  .person-name { font-size: 26px; line-height: 1.1; }
  .person-role { font-size: 11px; color: var(--ink-muted); margin-top: 2px; }

  .contact-list {
    position: absolute; left: 30px; top: 186px; list-style: none;
    color: var(--ink-light); font-size: 11px;
  }
  .contact-list li { display: flex; align-items: center; gap: 14px; height: 28px; }
  .contact-list svg { width: 18px; height: 18px; flex: none; }

  .address {
    position: absolute; left: 300px; top: 222px; display: flex; align-items: flex-start; gap: 12px;
    color: var(--ink-light); font-size: 11px; line-height: 17px;
  }
  .address svg { width: 14px; height: 14px; flex: none; margin-top: 1px; }
</style>
</head>
<body>
<main class="sheet">

  <section class="card card-front" aria-label="Business card, front">
    <svg class="card-bg" viewBox="0 0 520 297" preserveAspectRatio="none" aria-hidden="true">
      <defs>
        <linearGradient id="silver-band" x1="0" y1="0" x2="1" y2="1">
          <stop offset="0" stop-color="#c9c9c9"/>
          <stop offset="0.45" stop-color="#f1f1f1"/>
          <stop offset="1" stop-color="#c9c9c9"/>
        </linearGradient>
      </defs>
      <rect width="520" height="297" fill="#174560"/>
      <path d="M0 0 H520 V108 H24 V74 Q24 64 14 64 H0 Z" fill="url(#silver-band)"/>
    </svg>

    <div class="brand">
      <div class="brand-name">Quiet Harbour</div>
      <div class="brand-tagline">Tourism Marketing &amp; Representation</div>
    </div>

    <div class="person">
      <div class="person-name">Odette Farrow</div>
      <div class="person-role">Director</div>
    </div>

    <ul class="contact-list">
      <li>
        <svg viewBox="0 0 18 18" aria-hidden="true"><rect x="2" y="4" width="14" height="10" fill="none" stroke="currentColor" stroke-width="1.2"/><path d="M2 4 L9 10 L16 4" fill="none" stroke="currentColor" stroke-width="1.2"/></svg>
        <span class="contact-email">odette@quietharbour.com.au</span>
      </li>
      <li>
        <svg viewBox="0 0 18 18" aria-hidden="true"><rect x="5" y="1.5" width="8" height="15" rx="1.5" fill="none" stroke="currentColor" stroke-width="1.2"/><line x1="7.5" y1="14" x2="10.5" y2="14" stroke="currentColor" stroke-width="1.2"/></svg>
        <span class="contact-phone">+61 428306172</span>
      </li>
    </ul>

    <div class="address">
      <svg viewBox="0 0 16 16" aria-hidden="true"><path d="M8 2 L15 8 H13 V14 H9.5 V10 H6.5 V14 H3 V8 H1 Z" fill="currentColor"/></svg>
      <div>57 Wendlow Terrace<br>Harrowdene, Westmark, 2719 Australia</div>
    </div>
  </section>

  <section class="card card-back" aria-label="Business card, back">
    <div class="brand">
      <div class="brand-name">Quiet Harbour</div>
      <div class="brand-tagline">Tourism Marketing &amp; Representation</div>
    </div>
  </section>

</main>
</body>
</html>
```